Make my Product Label Stand out from the competition

My current product sells on pelmora, and needs a refreshed look to stay ahead of competition. We do need to keep some of the current branding in mind, as this brand has other products also, but let see where we can make some enhancements.

Logo Text

Beard Oil

```html
<!DOCTYPE html>
<html lang="en">
<head>
<meta charset="utf-8">
<title>Beard Oil – Product Label</title>
<link rel="stylesheet" href="https://fonts.googleapis.com/css2?family=Montserrat:wght@400;600;700&display=swap">
<style>
  :root {
    --backdrop: #e4e4e2;
    --label-paper: #fbfbfa;
    --label-edge: #dcdcd8;
    --ink: #1c1c1c;
    --ink-soft: #5a5a58;
    --amber: #e59a2f;
  }
  * { box-sizing: border-box; margin: 0; padding: 0; }
  html, body {
    width: 1200px;
    height: 900px;
    overflow: hidden;
    background: var(--backdrop);
    font-family: "Montserrat", sans-serif;
    color: var(--ink);
  }
  .canvas {
    width: 1200px;
    height: 900px;
    display: flex;
    align-items: center;
    justify-content: center;
  }
  .label {
    width: 1040px;
    height: 440px;
    background: var(--label-paper);
    border: 1px solid var(--label-edge);
    display: grid;
    grid-template-columns: 300px 440px 300px;
  }
  .panel {
    position: relative;
    padding: 40px 36px;
  }
  .panel--info {
    display: flex;
    align-items: center;
    gap: 30px;
  }
  .brand-vertical {
    writing-mode: vertical-rl;
    transform: rotate(180deg);
    font-weight: 400;
    font-size: 22px;
    letter-spacing: 0.14em;
    line-height: 1.5;
    text-transform: uppercase;
    text-align: center;
  }
  .info-copy {
    font-size: 13px;
    line-height: 1.7;
    color: var(--ink-soft);
  }
  .info-copy .web {
    display: block;
    margin-top: 18px;
    color: var(--ink);
  }
  .panel--title {
    display: flex;
    align-items: center;
    justify-content: center;
    gap: 16px;
  }
  .title-dot {
    width: 18px;
    height: 18px;
    border-radius: 50%;
    background: var(--amber);
    flex: none;
  }
  .product-name {
    font-weight: 700;
    font-size: 44px;
    line-height: 1;
    letter-spacing: 0.04em;
    text-transform: uppercase;
    color: var(--ink);
    white-space: nowrap;
  }
  .panel--directions {
    display: flex;
    align-items: center;
  }
  .directions-copy {
    font-size: 13px;
    line-height: 1.7;
    color: var(--ink-soft);
  }
  .directions-copy strong {
    display: block;
    color: var(--ink);
    font-weight: 600;
    letter-spacing: 0.08em;
    text-transform: uppercase;
    margin-bottom: 6px;
  }
</style>
</head>
<body>
<main class="canvas">
  <section class="label">
    <div class="panel panel--info">
      <h2 class="brand-vertical">Business<br>Name &amp; Co</h2>
      <p class="info-copy">
        Ingredients: argan oil, jojoba oil, sweet almond oil, vitamin E, cedarwood, bergamot.
        <span class="web">www.businessname.com</span>
      </p>
    </div>

    <div class="panel panel--title">
      <span class="title-dot" aria-hidden="true"></span>
      <h1 class="product-name">Beard Oil</h1>
    </div>

    <div class="panel panel--directions">
      <p class="directions-copy">
        <strong>Directions</strong>
        place three drops in palm, rub hands together and work through beard to the skin.
      </p>
    </div>
  </section>
</main>
</body>
</html>
```